Business Card

We need a business card designed using one of the attached logo designs (our preference is for the boxes version, but if you think it looks better with the horizontal version we will consider those too). Standard business card dimensions.

Details that need to be included:

Lewis Marsh
Quorvane S.L.U
lewis@quorvane.com

Phone numbers:
(UK) +44 731 4602 385
(Spain) +34 615 480 327

Twitter: @Quorvane
Web: http://www.quorvane.com

Tagline (optional, if it doesnt make it look too cluttered):
Automation and configuration management specialists
or
Configuration management specialists

```html
<!DOCTYPE html>
<html lang="en">
<head>
<meta charset="utf-8">
<title>Quorvane Business Card Options</title>
<link href="https://fonts.googleapis.com/css2?family=Source+Sans+3:wght@400;700&display=swap" rel="stylesheet">
<style>
  :root {
    --stage: #1f2222;
    --card: #ffffff;
    --ink: #1a1a1a;
    --accent: #1ea0dc;
    --band-start: #3fc3ee;
    --band-end: #4a8fcf;
    --mark: #3d9be0;
    --band-text: #ffffff;
  }
  * { margin: 0; padding: 0; box-sizing: border-box; }
  html, body { width: 1200px; height: 1000px; overflow: hidden; }
  body {
    background: var(--stage);
    font-family: "Source Sans 3", "Myriad Pro", sans-serif;
    position: relative;
  }
  .card {
    position: absolute;
    left: 334px;
    width: 528px;
    height: 301px;
    background: var(--card);
    overflow: hidden;
  }
  .card--corner { top: 30px; }
  .card--stacked { top: 347px; left: 335px; }
  .card--centered { top: 666px; }

  .brand {
    position: absolute;
    display: flex;
    align-items: center;
    gap: 6px;
    color: var(--ink);
    font-weight: 700;
    letter-spacing: 0.5px;
  }
  .brand__square {
    width: 37px; height: 37px;
    background: var(--mark);
    border-radius: 2px;
    flex: none;
  }
  .brand__name { font-size: 28px; line-height: 1; }
  .brand--corner { left: 11px; top: 10px; }
  .brand--centered { left: 165px; top: 14px; }
  .brand--stacked {
    left: 10px; top: 9px;
    flex-direction: column;
    gap: 4px;
  }
  .brand--stacked .brand__square { width: 78px; height: 78px; border-radius: 6px; }
  .brand--stacked .brand__name { font-size: 14.5px; }

  .contact {
    position: absolute;
    left: 0; right: 0;
    text-align: center;
    font-size: 22px;
    line-height: 29.5px;
    color: var(--ink);
  }
  .contact__name { color: var(--accent); font-weight: 700; font-size: 23px; }
  .card--corner .contact { top: 66px; }
  .card--stacked .contact { top: 55px; }
  .card--centered .contact { top: 71px; }

  .band {
    position: absolute;
    left: 0; right: 0; bottom: 0;
    height: 55px;
    background: linear-gradient(90deg, var(--band-start), var(--band-end));
    color: var(--band-text);
    font-size: 19.5px;
    display: flex;
    align-items: center;
    justify-content: space-between;
    padding: 0 15px 0 12px;
  }
</style>
</head>
<body>

<section class="card card--corner">
  <div class="brand brand--corner">
    <span class="brand__square"></span>
    <span class="brand__name">QUORVANE</span>
  </div>
  <div class="contact">
    <p class="contact__name">Lewis Marsh</p>
    <p>Quorvane S.L.U</p>
    <p>lewis@quorvane.com</p>
    <p>(UK) +44 731 4602 385</p>
    <p>(Spain) +34 615 480 327</p>
  </div>
  <footer class="band">
    <span>Twitter: @Quorvane</span>
    <span>www.quorvane.com</span>
  </footer>
</section>

<section class="card card--stacked">
  <div class="brand brand--stacked">
    <span class="brand__square"></span>
    <span class="brand__name">QUORVANE</span>
  </div>
  <div class="contact">
    <p class="contact__name">Lewis Marsh</p>
    <p>Quorvane S.L.U</p>
    <p>lewis@quorvane.com</p>
    <p>(UK) +44 731 4602 385</p>
    <p>(Spain) +34 615 480 327</p>
  </div>
  <footer class="band">
    <span>Twitter: @Quorvane</span>
    <span>www.quorvane.com</span>
  </footer>
</section>

<section class="card card--centered">
  <div class="brand brand--centered">
    <span class="brand__square"></span>
    <span class="brand__name">QUORVANE</span>
  </div>
  <div class="contact">
    <p class="contact__name">Lewis Marsh</p>
    <p>Quorvane S.L.U</p>
    <p>lewis@quorvane.com</p>
    <p>(UK) +44 731 4602 385</p>
    <p>(Spain) +34 615 480 327</p>
  </div>
  <footer class="band">
    <span>Twitter: @Quorvane</span>
    <span>www.quorvane.com</span>
  </footer>
</section>

</body>
</html>
```